Accident Law Firm Billboard Bold Easy to See Car Accidents

We need a billboard design that can catch attention in a very crowed Car Accident lawyer market. We wish to feature the phone number (652) 318-4470 as the focus of the Bill Board. We are trying to get the phone number recognized and remembered by drivers. The law firm name is not as crucial to remember.
Basically, It's CAR ACCIDENT? Then (652) 318-4470. We are not married to any specific color scheme but it has to POP and catch attention.
So the Crucial elements are as follows:
1. Phone number (652) 318-4470
2. Words CAR ACCIDENT?
3. Firm Logo in lower portion or where appropriate. Firm Logo to be provided
4. We may want to try a Day Glow orange color, with White and Black added. An example of the color scheme shall be provided.
5. Possible "Catch Phrase" to be used, "It's Time Call 9"
Target Market(s)
Orlando Florida Car Accident victims
Industry/Entity Type
Law Firm
Requirements
Must have
- Easy to see phone number (652) 318-4470
- Catch attention
Nice to have
- I would like to have the sign visible in bright sunlight and it not too hard to immediately know what phone number is for
Should not have
- too many words
- No bold enough
- confusing fonts
- Unclear fonts

```html
<!DOCTYPE html>
<html lang="en">
<head>
<meta charset="utf-8">
<title>Marrowind Law Firm – Car Accident Billboard</title>
<link href="https://fonts.googleapis.com/css2?family=Montserrat:wght@400;500;700;800;900&display=swap" rel="stylesheet">
<style>
  :root {
    --backdrop-top: #000000;
    --backdrop-bottom: #8a8b89;
    --board-white: #ffffff;
    --ink: #231f20;
    --dayglow-top: #ec3629;
    --dayglow-bottom: #f15a33;
    --shadow-red: #c7291d;
    --type-white: #ffffff;
  }
  * { margin: 0; padding: 0; box-sizing: border-box; }
  html, body {
    width: 1200px;
    height: 686px;
    overflow: hidden;
  }
  body {
    font-family: "Montserrat", sans-serif;
  }
  .stage {
    position: relative;
    width: 1200px;
    height: 686px;
    background: linear-gradient(to bottom, var(--backdrop-top) 0%, #1a1a1a 30%, var(--backdrop-bottom) 100%);
    overflow: hidden;
  }
  .billboard {
    position: absolute;
    left: 99px;
    top: 90px;
    width: 1002px;
    height: 506px;
    background: var(--board-white);
  }
  .firm-name {
    position: absolute;
    left: 0;
    right: 0;
    top: 50px;
    text-align: center;
    color: var(--ink);
    line-height: 1;
  }
  .firm-name__main {
    display: block;
    font-weight: 800;
    font-size: 44px;
    letter-spacing: 0.5px;
    margin-left: -16px;
  }
  .firm-name__sub {
    display: block;
    font-weight: 500;
    font-size: 25px;
    letter-spacing: 4px;
    margin-top: 2px;
    margin-left: -16px;
  }
  .headline {
    position: absolute;
    left: 0;
    right: 0;
    top: 150px;
    text-align: center;
    font-weight: 900;
    font-size: 94px;
    line-height: 1;
    color: var(--ink);
  }
  .call-band {
    position: absolute;
    left: 0;
    top: 262px;
    width: 100%;
    height: 230px;
    background: linear-gradient(to bottom, var(--dayglow-top), var(--dayglow-bottom) 45%);
  }
  .catch-phrase {
    position: absolute;
    left: 0;
    right: 0;
    top: 34px;
    text-align: center;
    color: var(--type-white);
    font-weight: 400;
    font-size: 62px;
    line-height: 1;
    text-shadow: 3px 3px 0 var(--shadow-red);
  }
  .phone-number {
    position: absolute;
    left: 0;
    right: 0;
    top: 110px;
    text-align: center;
    color: var(--type-white);
    font-weight: 700;
    font-size: 104px;
    line-height: 1;
    letter-spacing: 1px;
    text-shadow: 4px 4px 0 var(--shadow-red);
  }
  .base-strip {
    position: absolute;
    left: 0;
    bottom: 0;
    width: 100%;
    height: 14px;
    background: var(--ink);
  }
</style>
</head>
<body>
  <main class="stage">
    <section class="billboard">
      <div class="firm-name">
        <span class="firm-name__main">MARROWIND</span>
        <span class="firm-name__sub">LAW FIRM P.C</span>
      </div>
      <h1 class="headline">CAR ACCIDENT?</h1>
      <div class="call-band">
        <p class="catch-phrase">IT’S TIME CALL 9</p>
        <p class="phone-number">(652) 318-4470</p>
      </div>
      <div class="base-strip"></div>
    </section>
  </main>
</body>
</html>
```